Flyer Design

We are a property company and need attractive flyers that will grab peoples attention. We want them to be bold but simple and not too busy. I attach a draft and also our logo. We will print in A5 size.
Thank you & I look forward to receiving designs.

It Company

```html
<!DOCTYPE html>
<html lang="en">
<head>
<meta charset="utf-8">
<title>Kora Developments – Subdivision Flyer</title>
<link href="https://fonts.googleapis.com/css2?family=Open+Sans:wght@600;700&display=swap" rel="stylesheet">
<style>
  :root {
    --paper: #ffffff;
    --brand-band: #e6dac8;
    --brand-ink: #8a6b4b;
    --sky-top: #7fb2e0;
    --sky-low: #cfe0ee;
    --lawn: #6e8a3c;
    --accent-red: #b8372b;
    --deep-black: #141414;
    --ink: #111111;
    --light: #ffffff;
  }
  * { margin: 0; padding: 0; box-sizing: border-box; }
  html, body { width: 869px; height: 1200px; overflow: hidden; background: var(--paper); }
  body { font-family: "Open Sans", Arial, sans-serif; }
  .flyer { position: relative; width: 869px; height: 1200px; background: var(--paper); }

  .brand-band {
    position: absolute; left: 20px; top: 20px; width: 829px; height: 130px;
    background: linear-gradient(90deg, #e9dfcf, #e1d3bf 50%, #e9dfcf);
    display: flex; align-items: center; justify-content: center; gap: 14px;
  }
  .brand-mark { width: 22px; height: 22px; background: var(--brand-ink); }
  .brand-name {
    font-weight: 700; font-size: 34px; letter-spacing: 2px;
    color: var(--brand-ink); text-transform: uppercase;
  }

  .hero-photo {
    position: absolute; left: 20px; top: 150px; width: 829px; height: 450px;
    background: linear-gradient(180deg, var(--sky-top) 0%, var(--sky-low) 45%, #b9a98c 62%, var(--lawn) 100%);
  }

  .headline-ribbon { position: absolute; left: 20px; top: 540px; width: 840px; height: 170px; }
  .headline-ribbon svg { position: absolute; inset: 0; }
  .headline-text {
    position: absolute; left: 24px; top: 12px; width: 760px;
    color: var(--light); font-weight: 700; font-size: 33px; line-height: 41px;
  }

  .pitch {
    position: absolute; left: 0; width: 869px; text-align: center;
    color: var(--ink); font-weight: 700; font-size: 30px; line-height: 44px;
  }
  .pitch-question { top: 748px; }
  .pitch-offer { top: 812px; }

  .contact-box {
    position: absolute; left: 20px; top: 944px; width: 829px; height: 152px;
    background: var(--accent-red); color: var(--light);
    font-weight: 700; font-size: 25.5px; line-height: 44px;
    padding: 16px 0 0 44px;
  }
  .web-bar {
    position: absolute; left: 20px; top: 1096px; width: 829px; height: 84px;
    background: var(--deep-black); color: var(--light);
    font-weight: 700; font-size: 40px; text-align: center; line-height: 84px;
  }
</style>
</head>
<body>
<main class="flyer">
  <header class="brand-band">
    <span class="brand-mark"></span>
    <span class="brand-name">Kora Developments</span>
  </header>

  <div class="hero-photo" role="img" aria-label="Photo of a row of suburban weatherboard houses with lawns under a blue sky"></div>

  <section class="headline-ribbon">
    <svg width="840" height="170" viewBox="0 0 840 170" aria-hidden="true">
      <polygon points="0,22 830,22 782,168 0,168" fill="var(--deep-black)"/>
      <polygon points="0,0 812,0 766,142 0,142" fill="var(--accent-red)"/>
    </svg>
    <h1 class="headline-text">Are you a home owner looking for financial freedom while been able to keep your own&nbsp; home?</h1>
  </section>

  <p class="pitch pitch-question">Are you struggling to pay your mortgage?</p>
  <p class="pitch pitch-offer">KORA specialise in subdivisions including<br>finance and management.</p>

  <section class="contact-box">
    Call 021 555 018 or email info@korasubdivisions.com<br>
    for more information or to find out ifyour property is<br>
    suitable for subdivision in Auckland.
  </section>

  <footer class="web-bar">www.korasubdivisions.com</footer>
</main>
</body>
</html>
```